Business Card Design Project

Need business card for new non profit organization that includes the attached logo in some form.
with this information
Name: Michael Dorrance Pilbeam
Title: President & Founder
A: P.O. Box 51607, Portland, Oregon, 97214-5160
E: mike@dorrancetrust.org
E: mike@mikepilbeam.com
P: 1.971.555.0172

Industry/Entity Type
Non Profit

```html
<!DOCTYPE html>
<html lang="en">
<head>
<meta charset="utf-8">
<title>Dorrance Trust – Business Card</title>
<link rel="stylesheet" href="https://fonts.googleapis.com/css2?family=Tinos:wght@400&display=swap">
<style>
  :root {
    --navy: #00226a;
    --navy-light: #2a4a94;
    --white: #ffffff;
    --ink: #1c1c1c;
    --page: #eef0f3;
    --silver-dark: #2a2826;
    --silver-mid: #a9a9aa;
    --silver-light: #ffffff;
    --silver-pale: #d6dbd9;
  }
  * { box-sizing: border-box; margin: 0; padding: 0; }
  html, body {
    width: 1200px;
    height: 900px;
    overflow: hidden;
    background: var(--page);
    font-family: "Tinos", "Times New Roman", serif;
  }
  .canvas {
    position: relative;
    width: 1200px;
    height: 900px;
  }
  .card {
    position: absolute;
    width: 640px;
    height: 370px;
    background: var(--white);
    overflow: hidden;
  }

  /* Back face */
  .card-back { left: 280px; top: 55px; }
  .card-back .brand {
    position: absolute;
    left: 0; right: 0; top: 140px;
    display: flex;
    align-items: center;
    justify-content: center;
    gap: 22px;
  }
  .card-back .brand-mark {
    width: 64px; height: 64px;
    border-radius: 50%;
    background: var(--navy);
  }
  .card-back .brand-name {
    color: var(--navy);
    font-size: 52px;
    letter-spacing: 0.5px;
  }
  .card-back .base-band {
    position: absolute;
    left: 0; right: 0; bottom: 0;
    height: 20px;
    background: var(--navy);
  }

  /* Front face */
  .card-front { left: 280px; top: 475px; }
  .card-front .brand {
    position: absolute;
    left: 40px; top: 62px;
    display: flex;
    align-items: center;
    gap: 14px;
  }
  .card-front .brand-mark {
    width: 38px; height: 38px;
    border-radius: 50%;
    background: var(--navy);
  }
  .card-front .brand-name {
    color: var(--navy);
    font-size: 32px;
  }
  .holder-name {
    position: absolute;
    right: 60px; top: 156px;
    font-size: 26px;
    color: var(--ink);
  }
  .title-band {
    position: absolute;
    left: 0; right: 0; top: 194px;
    height: 36px;
    background: linear-gradient(90deg,
      var(--silver-dark) 0%,
      var(--silver-mid) 9%,
      var(--silver-light) 24%,
      var(--silver-pale) 38%,
      var(--silver-mid) 62%,
      #8f8d8c 80%,
      var(--silver-dark) 100%);
  }
  .holder-title {
    position: absolute;
    right: 60px; top: 6px;
    font-size: 19px;
    color: var(--white);
  }
  .contact-panel {
    position: absolute;
    left: 0; right: 0; top: 230px; bottom: 0;
    background: var(--navy);
    color: var(--white);
  }
  .contact-item {
    position: absolute;
    display: flex;
    align-items: center;
    gap: 10px;
    white-space: nowrap;
  }
  .contact-item svg { fill: none; stroke: var(--white); }
  .phone { left: 42px; top: 28px; font-size: 19px; }
  .address { left: 42px; top: 69px; font-size: 14px; }
  .email-main { left: 366px; top: 31px; font-size: 15px; }
  .email-alt { left: 392px; top: 68px; font-size: 15px; }
</style>
</head>
<body>
<main class="canvas">

  <section class="card card-back" aria-label="Business card, back">
    <div class="brand">
      <span class="brand-mark"></span>
      <span class="brand-name">Dorrance Trust</span>
    </div>
    <div class="base-band"></div>
  </section>

  <section class="card card-front" aria-label="Business card, front">
    <div class="brand">
      <span class="brand-mark"></span>
      <span class="brand-name">Dorrance Trust</span>
    </div>

    <h1 class="holder-name" style="font-weight:400">Michael Dorrance Pilbeam</h1>

    <div class="title-band">
      <p class="holder-title">President &amp; Founder</p>
    </div>

    <div class="contact-panel">
      <p class="contact-item phone">
        <svg width="10" height="16" viewBox="0 0 10 16" aria-hidden="true">
          <path d="M3 2 Q8 2 8 8 Q8 14 3 14" stroke-width="2.4" stroke-linecap="round"/>
        </svg>
        1.971.555.0172
      </p>
      <p class="contact-item address">
        <svg width="12" height="16" viewBox="0 0 12 16" aria-hidden="true">
          <path d="M6 15 C2 10 1 8 1 6 A5 5 0 0 1 11 6 C11 8 10 10 6 15 Z" stroke-width="1.6"/>
          <circle cx="6" cy="6" r="1.8" stroke-width="1.4"/>
        </svg>
        P.O. Box 51607, Portland, Oregon, 97214-5160
      </p>
      <p class="contact-item email-main">
        <svg width="14" height="11" viewBox="0 0 14 11" aria-hidden="true">
          <rect x="0.7" y="0.7" width="12.6" height="9.6" stroke-width="1.2"/>
          <path d="M0.7 0.7 L7 6 L13.3 0.7" stroke-width="1.2"/>
        </svg>
        mike@dorrancetrust.org
      </p>
      <p class="contact-item email-alt">mike@mikepilbeam.com</p>
    </div>
  </section>

</main>
</body>
</html>
```